Catalogue 2-Page Cover Design

We are a U.S. company that makes and sells functional glass art products. All of our product are hand blown by our artisans. We need your talents and skills to help us make the cover pages of our 2014 catalogue. 2 pages, front (cover 1)and back(cover 2). Here to make things easier we calll it cover 1 and cover 2. Cover 2 should be designed upside down because we need it to be the front page when you flip the catalogue and start reading from the end. This is for the year 2014 so put "2014" on both Cover 1 and Cover 2 please.
The Cover 1 and Cover 2 won't be showing similar content because the "two front pages" lead you to different part of content.
The spine of the book will be 1.5 inch (1.5 inch thick). We need this part to be designed sharp and can pop up on a book shelf from all other books. Our company name should be on it. It can be colorful but no product pics.
Here is what we would want for Cover1 and 2 section:
COVER 1: cover 1 should artisticly present four categories products: Lighting, Wall art Plate, Table Top, and Chandeliers(the curily glass one). Please use pics attached in your design(named under Cover 1-abcd).
COVER2: This cover lead our readers to the contract/project section of the catalogue. We produce custom fixtures and really want to expand our market for the product. We want to draw in designers and customers that are looking for larger-scale lighting product. The cover need to instantly convey a high-end, luxurious but chic installation site.Please use the pic attached under name Cover 2-a in your design. Please convey our CAPABILITY of turning concept and design into real product. One way we are looking at is a mix of the sketch or drawing and the real product. (expample: left side pencil/pen sketch-right side real chandelier.) Please use the product in the pic attached (under name Cover 2-a) in your design. You can use PS to take the product out and put it into any background or settings you like.
We don't want to make very specific and detailed guidlines for that will limit your creativity. We are a pioneer glass art manufacture which breathed new life into a traditional art form. Please show your creativity and make a elegant but cool cover.
Attached files-
1. Catalogue inter pages examples-for a better understanding of our product and this catalogue, to better match the covers with inner pages.
2. Product pictures (Named Cover 1- a,b, c, d and Cover 2-a) - use those pics for your design.
3. Logo-The high res logo pic is also attached. should be put what ever most suitable in your design.
***A4 PAPER***
***Due Date is Monday, Jan 20th ***
Thanks for your time and effort in paticipating in this contest. We welcome any comments and questions.
Target Market(s)
our customers are: Interior Designers, Furnishing Stores, Hotels and Resorts, Art Galleris, Art Museums, Home and Decor Department Stores.
Industry/Entity Type
It Company
Requirements
Must have
- our company info, logo(attached) and other info below:
Quorlen Crafts Inc.
Corporate Office
4817 Maple Hollow Lane, San Leandro, CA 94578
Tel: 510-732-4061
Fax:510-732-4063
Email: info@quorlenworks.example
Website: www.quorlenworks.example
Nice to have
- Be artistic, be special and be cool.
Should not have
- Pictures not related to our company info and products.
Please use only Cover 1-a,b,c,d and Cover 2-a for your design. All other pics are inner page samples to give you a feel of our catalogue.

```html
<!DOCTYPE html>
<html lang="en">
<head>
<meta charset="utf-8">
<title>Quorlen Crafts 2014 Catalogue Cover Spread</title>
<link href="https://fonts.googleapis.com/css2?family=Arimo:wght@400&family=Cinzel:wght@700&family=Tinos:wght@400&display=swap" rel="stylesheet">
<style>
  :root {
    --ink: #0b0b0b;
    --paper: #ffffff;
    --stage: #f2f2f2;
    --gold: #e8c53a;
    --gold-line: #a88d35;
    --brand-blue: #2a8fd0;
    --text-light: #d8d8d8;
  }
  * { box-sizing: border-box; margin: 0; padding: 0; }
  html, body { width: 900px; height: 1200px; overflow: hidden; background: var(--stage); }
  .canvas { position: relative; width: 900px; height: 1200px; }

  .spread {
    position: absolute; left: 20px; top: 321px;
    width: 860px; height: 558px; display: flex;
    box-shadow: 0 2px 10px rgba(0,0,0,.25);
  }
  .cover, .spine { position: relative; height: 558px; overflow: hidden; }
  .cover { width: 394px; }
  .spine { width: 72px; background: var(--ink); border-left: 1px solid #333; border-right: 1px solid #333; }

  .year {
    font-family: "Cinzel", "Times New Roman", serif; font-weight: 700;
    color: var(--gold); letter-spacing: .5px;
  }
  .brand-name {
    font-family: "Arimo", Arial, sans-serif; font-weight: 400;
    color: var(--brand-blue); white-space: nowrap;
    display: flex; align-items: center; gap: 6px;
  }
  .brand-name .mark { width: 10px; height: 10px; background: var(--brand-blue); flex: none; }

  /* Back cover: project section, printed upside down */
  .cover--back { background: var(--ink); }
  .cover--back .upright { position: absolute; inset: 0; transform: rotate(180deg); }
  .project-photo {
    position: absolute; left: 32px; top: 50px; width: 330px; height: 440px;
    border: 1px solid var(--gold-line);
    background:
      radial-gradient(ellipse 22% 40% at 55% 45%, rgba(230,60,30,.85), rgba(240,210,40,.7) 35%, rgba(60,170,80,.6) 55%, rgba(40,90,210,.6) 75%, rgba(120,70,170,0) 100%),
      linear-gradient(180deg, #8c8c8c 0%, #cfcfcf 35%, #a8a8a8 65%, #e2e2e2 100%);
  }
  .cover--back .logo-tab {
    position: absolute; left: 0; top: 138px; width: 104px; height: 88px;
    background: var(--paper); border: 1px solid var(--gold-line);
    display: flex; align-items: center; justify-content: center;
  }
  .cover--back .logo-tab .brand-name { font-size: 10px; }
  .contact-bar {
    position: absolute; left: 32px; right: 32px; top: 503px; height: 40px;
    display: flex; align-items: center;
    font-family: "Tinos", "Times New Roman", serif; font-size: 7.5px; line-height: 1.4;
    color: var(--text-light);
  }
  .contact-bar .col { padding: 0 10px; height: 100%; display: flex; flex-direction: column; justify-content: center; }
  .contact-bar .col:first-child { padding-left: 0; }
  .contact-bar .col + .col { border-left: 1px solid #777; }
  .contact-bar .year { font-size: 21px; margin-left: auto; padding-left: 14px; border-left: 1px solid #777; height: 100%; display: flex; align-items: center; }

  /* Spine */
  .spine .year { position: absolute; left: 0; width: 100%; text-align: center; font-size: 17px; }
  .spine .year--top { top: 48px; }
  .spine .year--bottom { bottom: 48px; transform: rotate(180deg); }
  .spine .logo-tab {
    position: absolute; left: 0; top: 190px; width: 100%; height: 160px;
    background: var(--paper); display: flex; align-items: center; justify-content: center;
  }
  .spine .logo-tab .brand-name { transform: rotate(90deg); font-size: 12px; }

  /* Front cover: product section */
  .cover--front { background: var(--ink); }
  .hero {
    position: absolute; left: 0; top: 0; width: 100%; height: 314px; background: var(--paper);
  }
  .hero-photo {
    position: absolute; left: 0; top: 18px; width: 290px; height: 250px;
    background: radial-gradient(ellipse 50% 45% at 50% 55%, #d9b979 0%, #e9d8b2 45%, #ffffff 80%);
  }
  .hero .brand-name { position: absolute; right: 22px; top: 60px; font-size: 13px; }
  .product-row {
    position: absolute; left: 0; top: 325px; width: 100%; height: 165px; display: flex;
  }
  .product-row .tile { height: 100%; }
  .tile--vase { width: 140px; background: radial-gradient(ellipse 45% 50% at 50% 50%, #e8c22a 0%, #d6a21e 55%, #b98c2a 100%); }
  .tile--sculpture { width: 115px; background: radial-gradient(ellipse 55% 45% at 50% 45%, #3f79b3 0%, #3a4c5a 55%, #2a2f33 100%); }
  .tile--plate { width: 139px; background: radial-gradient(circle at 60% 50%, #d3210f 0%, #e43a20 42%, #ffffff 62%); }
  .footer-band {
    position: absolute; left: 0; top: 490px; width: 100%; height: 68px;
    border-top: 1px solid var(--gold-line);
    display: flex; align-items: center; justify-content: space-between;
    padding: 0 22px 0 130px;
  }
  .footer-band .web { font-family: "Arimo", Arial, sans-serif; font-size: 10px; color: var(--gold); }
  .footer-band .year { font-size: 22px; }
</style>
</head>
<body>
<main class="canvas">
  <section class="spread" aria-label="Quorlen Crafts 2014 catalogue cover spread">

    <article class="cover cover--back" aria-label="Cover 2, project section, printed upside down">
      <div class="upright">
        <div class="project-photo" role="img" aria-label="Large rainbow glass chandelier hanging in a grey multi-storey atrium with a spiral staircase"></div>
        <div class="logo-tab"><span class="brand-name"><span class="mark"></span>Quorlen Crafts</span></div>
        <footer class="contact-bar">
          <div class="col">
            <span>Quorlen Crafts Inc. Corporate Office</span>
            <span>4817 Maple Hollow Lane</span>
            <span>San Leandro, CA 94578</span>
          </div>
          <div class="col">
            <span>T 510-732-4061 | F 510-732-4063</span>
            <span>Email: info@quorlenworks.example</span>
            <span>Website: www.quorlenworks.example</span>
          </div>
          <span class="year">2014</span>
        </footer>
      </div>
    </article>

    <aside class="spine" aria-label="Spine">
      <span class="year year--top">2014</span>
      <div class="logo-tab"><span class="brand-name"><span class="mark"></span>Quorlen Crafts</span></div>
      <span class="year year--bottom">2014</span>
    </aside>

    <article class="cover cover--front" aria-label="Cover 1, product section">
      <div class="hero">
        <div class="hero-photo" role="img" aria-label="Amber glass chandelier with curled arms and candle lights on white"></div>
        <span class="brand-name"><span class="mark"></span>Quorlen Crafts</span>
      </div>
      <div class="product-row">
        <div class="tile tile--vase" role="img" aria-label="Yellow hand blown table top vase with abstract colour patches"></div>
        <div class="tile tile--sculpture" role="img" aria-label="Blue and green curly glass chandelier on a dark background"></div>
        <div class="tile tile--plate" role="img" aria-label="Red glass wall art plate with a speckled centre"></div>
      </div>
      <footer class="footer-band">
        <span class="web">www.quorlenworks.example</span>
        <span class="year">2014</span>
      </footer>
    </article>

  </section>
</main>
</body>
</html>
```